New Stationary and Logo Design for Start Up Company

We need a logo design and stationary set including letterhead, business card (double sided), compliments slip and envelope for a new company Bright Quill Media.
The files should be editable to update address and standard contact details, will need to forward to web designer and stationary printer.
The company will be an online marketer and distributer of various business education products in Australia.
The designs should convey simple clean image
Target Market(s)
Small business owners and professional service providers (ie Accountants, Lawyers, Real Estate Agents) in Australia
Industry/Entity Type
Education
Look and feel
Each slider illustrates characteristics of the customer's brand and the style your logo design should communicate.

```html
<!DOCTYPE html>
<html lang="en">
<head>
<meta charset="utf-8">
<title>Bright Quill Media – Header Band</title>
<link rel="stylesheet" href="https://fonts.googleapis.com/css2?family=Arimo:wght@400;700&display=swap">
<style>
  :root {
    --page-bg: #ffffff;
    --band-bg: #4b5660;
    --accent-blue: #1b9ad6;
    --text-light: #ffffff;
    --text-soft: #e6eaed;
  }
  html, body {
    margin: 0;
    padding: 0;
    width: 1200px;
    height: 234px;
    overflow: hidden;
    background: var(--page-bg);
    font-family: "Arimo", Helvetica, Arial, sans-serif;
  }
  .canvas {
    position: relative;
    width: 1200px;
    height: 234px;
  }
  .header-band {
    position: absolute;
    left: 35px;
    top: 39px;
    width: 1130px;
    height: 162px;
    background: var(--band-bg);
    box-shadow: 0 1px 4px rgba(0, 0, 0, 0.35);
  }
  .brand-name {
    position: absolute;
    left: 58px;
    top: 21px;
    margin: 0;
    font-size: 30px;
    font-weight: 400;
    letter-spacing: -1px;
    color: var(--text-light);
    line-height: 1;
  }
  .contact-block {
    position: absolute;
    left: 883px;
    top: 67px;
    height: 72px;
  }
  .contact-bracket {
    position: absolute;
    left: 0;
    top: 0;
  }
  .contact-list {
    position: absolute;
    left: 23px;
    top: 4px;
    margin: 0;
    padding: 0;
    list-style: none;
    font-size: 12.5px;
    line-height: 15px;
    color: var(--text-soft);
    white-space: nowrap;
  }
  .contact-label {
    font-weight: 700;
    color: var(--text-light);
  }
</style>
</head>
<body>
<div class="canvas">
  <header class="header-band">
    <h1 class="brand-name">Bright Quill Media</h1>

    <div class="contact-block">
      <svg class="contact-bracket" width="16" height="72" viewBox="0 0 16 72" aria-hidden="true">
        <path d="M14 0 H2 V72 H14" fill="none" stroke="var(--accent-blue)" stroke-width="4"/>
      </svg>
      <ul class="contact-list">
        <li><span class="contact-label">adress:</span> 2718 Harbour View Road</li>
        <li><span class="contact-label">tel:</span> 612.430.7785</li>
        <li><span class="contact-label">e-mail:</span> info@brightquill.com.au</li>
        <li><span class="contact-label">web:</span> www.brightquill.com.au</li>
      </ul>
    </div>
  </header>
</div>
</body>
</html>
```